Lumora aesthetics offers a range of facial aesthetics treatments by a fully qualified dentist, to a high end crowd. Treatments include antiwrinkle treatment, the use of dermal fillers to provide facial volumisation and rejuvenation and also lip volumisation.
I want a luxurious and bold look. Black background with a bold striking gold logo in the centre possibly incorporating the outline of a face in a subtle yet effective way. I want it to include the work I offer so people will be aware of what they are looking into but not look like there's too much on the card, So it's a clean look.
At the bottom I would like it to say by Dr. Meera Sandhu. Alongside my email address and mobile number.

```html
<!DOCTYPE html>
<html lang="en">
<head>
<meta charset="utf-8">
<title>Lumora aesthetics – business card</title>
<link href="https://fonts.googleapis.com/css2?family=Jost:wght@400;700&display=swap" rel="stylesheet">
<style>
  :root {
    --page-bg: #ece9e4;
    --card-black: #2b2b2c;
    --card-black-deep: #1f1f20;
    --card-white: #fbfbfa;
    --gold-light: #f1e07a;
    --gold-mid: #d9b43c;
    --gold-deep: #d0861f;
    --gold-text: #dcb84a;
    --gold-soft: #c9b274;
    --ink: #1d1d1d;
    --ink-soft: #333333;
  }
  * { box-sizing: border-box; margin: 0; padding: 0; }
  html, body {
    width: 1200px;
    height: 788px;
    overflow: hidden;
    background: var(--page-bg);
    font-family: "Jost", "Helvetica Neue", Arial, sans-serif;
  }
  .sheet {
    position: relative;
    width: 1200px;
    height: 788px;
    display: flex;
    align-items: center;
    justify-content: center;
    gap: 50px;
  }
  .card {
    position: relative;
    width: 525px;
    height: 300px;
    overflow: hidden;
    box-shadow: 0 10px 28px rgba(0, 0, 0, 0.18);
  }

  /* Front side */
  .card--front {
    background: linear-gradient(135deg, var(--card-black) 0%, var(--card-black-deep) 100%);
  }
  .card--front .gold-profile {
    position: absolute;
    left: 0;
    top: 0;
    width: 56%;
    height: 100%;
  }
  .brand {
    position: absolute;
    left: 56%;
    right: 0;
    top: 0;
    bottom: 0;
    display: flex;
    flex-direction: column;
    align-items: center;
    justify-content: center;
    text-align: center;
    padding: 0 16px;
  }
  .brand__mark {
    width: 12px;
    height: 12px;
    border-radius: 50%;
    background: var(--gold-text);
    margin-bottom: 14px;
  }
  .brand__name {
    font-weight: 700;
    font-size: 24px;
    line-height: 1.15;
    letter-spacing: 1px;
    color: var(--gold-text);
  }
  .treatments {
    list-style: none;
    margin-top: 18px;
    padding-top: 14px;
    border-top: 1px solid var(--gold-soft);
    width: 150px;
  }
  .treatments li {
    font-weight: 400;
    font-size: 12px;
    line-height: 1.6;
    letter-spacing: 1px;
    text-transform: uppercase;
    color: var(--gold-soft);
  }

  /* Back side */
  .card--back {
    background: var(--card-white);
  }
  .card--back .gold-profile {
    position: absolute;
    left: 0;
    top: 0;
    width: 62%;
    height: 100%;
  }
  .contact {
    position: absolute;
    right: 22px;
    top: 20px;
    height: 260px;
    writing-mode: vertical-rl;
    color: var(--ink);
  }
  .contact__name {
    font-weight: 700;
    font-size: 24px;
    letter-spacing: 0.5px;
    line-height: 1.3;
    margin-left: 10px;
  }
  .contact__line {
    font-weight: 400;
    font-size: 16px;
    line-height: 1.35;
    color: var(--ink-soft);
  }
</style>
</head>
<body>
  <main class="sheet">
    <section class="card card--front" aria-label="Card front">
      <svg class="gold-profile" role="img" aria-label="Gold foil area with the profile silhouette of a woman's face" viewBox="0 0 294 300" preserveAspectRatio="none">
        <defs>
          <linearGradient id="gold-front" x1="0.9" y1="0" x2="0" y2="1">
            <stop offset="0" stop-color="#f1e07a"/>
            <stop offset="0.55" stop-color="#d9b43c"/>
            <stop offset="1" stop-color="#d0861f"/>
          </linearGradient>
        </defs>
        <rect width="294" height="300" fill="url(#gold-front)"/>
      </svg>
      <div class="brand">
        <span class="brand__mark" aria-hidden="true"></span>
        <p class="brand__name">Lumora<br>aesthetics</p>
        <ul class="treatments">
          <li>Anti-wrinkle</li>
          <li>Dermal fillers</li>
          <li>Lip volumisation</li>
        </ul>
      </div>
    </section>

    <section class="card card--back" aria-label="Card back">
      <svg class="gold-profile" role="img" aria-label="Gold foil area with the profile silhouette of a woman's face" viewBox="0 0 326 300" preserveAspectRatio="none">
        <defs>
          <linearGradient id="gold-back" x1="0.9" y1="0" x2="0" y2="1">
            <stop offset="0" stop-color="#f1e07a"/>
            <stop offset="0.55" stop-color="#d9b43c"/>
            <stop offset="1" stop-color="#d0861f"/>
          </linearGradient>
        </defs>
        <rect width="326" height="300" fill="url(#gold-back)"/>
      </svg>
      <div class="contact">
        <p class="contact__name">Dr. Meera Sandhu</p>
        <p class="contact__line">meera.sandhu@lumoramail.com</p>
        <p class="contact__line">01/98765432</p>
      </div>
    </section>
  </main>
</body>
</html>
```